New Business Cards / Logo update

Logo:
can be updated but wanted pricing

New Business Cards:
take our existing business cards and upgrade them from a design perspective. We have two versions
Inside sales team does not have a cell phone and they use an appointment back slot.
Outside project managers and leadership uses a slogan backing and will have cell phones.

```html
<!DOCTYPE html>
<html lang="en">
<head>
<meta charset="utf-8">
<title>Keystone Carpet + Flooring — Business Cards</title>
<link rel="stylesheet" href="https://fonts.googleapis.com/css2?family=Libre+Caslon+Text&family=Cormorant+Garamond:ital@1&family=Poppins:wght@400;500&display=swap">
<style>
  :root {
    --orange: #e08b26;
    --grey: #8f8681;
    --grey-light: #e4e1de;
    --ink: #1d1d1d;
    --card: #ffffff;
    --backdrop: #6e4e30;
  }
  * { box-sizing: border-box; margin: 0; padding: 0; }
  html, body { width: 1200px; height: 2315px; overflow: hidden; }
  body { background: var(--backdrop); position: relative; font-family: "Poppins", sans-serif; }

  .card {
    position: absolute; left: 189px; width: 836px; height: 477px;
    background: var(--card); border-radius: 37px; overflow: hidden;
    box-shadow: 0 6px 14px rgba(0,0,0,.35);
  }
  .card > * { position: absolute; }

  /* Front */
  .company-name {
    left: 40px; top: 62px; width: 420px;
    font-family: "Poppins", sans-serif; font-weight: 500; font-size: 40px; line-height: 1.15;
    color: var(--orange);
  }
  .motto { right: 40px; top: 70px; font-family: "Cormorant Garamond", serif; font-style: italic; font-size: 66px; color: var(--grey-light); line-height: 1; }
  .person { left: 40px; top: 257px; font-family: "Libre Caslon Text", serif; }
  .person-name { display: block; color: var(--orange); font-size: 33px; line-height: 1.1; }
  .person-role { display: block; color: var(--ink); font-size: 21px; line-height: 1.2; }
  .rule { left: 40px; right: 41px; top: 318px; height: 1px; background: var(--grey); }
  .contact { left: 40px; top: 365px; list-style: none; color: var(--grey); font-size: 22px; line-height: 27px; }
  .contact li { display: flex; align-items: center; gap: 9px; }
  .icon { width: 25px; height: 25px; background: var(--orange); border-radius: 4px; display: inline-flex; align-items: center; justify-content: center; }
  .address { right: 41px; top: 365px; text-align: right; color: var(--grey); font-size: 22px; line-height: 27px; font-style: normal; }
  .stripe { left: 0; bottom: 0; width: 836px; height: 40px; }

  /* Back */
  .headline { left: 0; right: 0; text-align: center; color: var(--grey); font-size: 44px; line-height: 1; }
  .headline-lead { font-family: "Poppins", sans-serif; font-weight: 500; color: var(--orange); font-size: 62px; }
  .headline-line2 { display: block; margin-top: 8px; }
  .days { left: 64px; right: 40px; top: 278px; display: flex; list-style: none; }
  .days li { width: 124px; display: flex; align-items: flex-end; gap: 20px; font-size: 21px; color: var(--ink); }
  .box { width: 29px; height: 29px; border: 1px solid #555; flex: none; }
  .slot { left: 65px; top: 338px; width: 705px; height: 50px; font-size: 23px; color: var(--ink); }
  .slot > * { position: absolute; }
  .slot-line { height: 1px; background: #555; top: 25px; }
  .meridiem { left: 670px; top: -7px; line-height: 20px; font-size: 23px; }
  .web {
    left: 0; bottom: 0; width: 100%; height: 52px; background: var(--orange);
    color: #fff; font-size: 22px; letter-spacing: .3em; text-align: center; line-height: 52px; font-weight: 500;
  }
</style>
</head>
<body>

<!-- Inside sales: front -->
<section class="card card-front" style="top:118px">
  <p class="company-name">Keystone<br>Carpet + Flooring</p>
  <p class="motto">craft first</p>
  <div class="person"><span class="person-name">Dana Whitfield</span><span class="person-role">General Manager</span></div>
  <div class="rule"></div>
  <ul class="contact">
    <li><span class="icon"><svg width="15" height="15" viewBox="0 0 24 24"><path fill="#fff" d="M6.6 10.8a15 15 0 0 0 6.6 6.6l2.2-2.2c.3-.3.7-.4 1-.2 1.1.4 2.300.6 3.6.6.6 0 1 .4 1 1V20c0 .6-.4 1-1 1A17 17 0 0 1 3 4c0-.6.4-1 1-1h3.5c.6 0 1 .4 1 1 0 1.3.2 2.5.6 3.6.1.3 0 .7-.2 1z"/></svg></span>800 555 0142</li>
    <li><span class="icon"><svg width="16" height="12" viewBox="0 0 16 12"><rect x="1" y="1" width="14" height="10" fill="none" stroke="#fff" stroke-width="1.4"/><path d="M1 1l7 6 7-6" fill="none" stroke="#fff" stroke-width="1.4"/></svg></span>keystonefloors@mailbox.net</li>
  </ul>
  <address class="address">1470 Harbor Mill Rd.<br>Venice, FL 34285</address>
  <svg class="stripe" viewBox="0 0 836 40"><path d="M0 18H470L464 40H0Z" fill="#8f8681"/><path d="M484 0H836V40H476Z" fill="#e08b26"/></svg>
</section>

<!-- Inside sales: appointment back -->
<section class="card card-back" style="top:620px">
  <p class="headline" style="top:74px"><span class="headline-lead">Keystone</span> flooring at<span class="headline-line2">an affordable price</span></p>
  <ul class="days">
    <li><span class="box"></span>Mon</li>
    <li><span class="box"></span>Tues</li>
    <li><span class="box"></span>Wed</li>
    <li><span class="box"></span>Thur</li>
    <li><span class="box"></span>Fri</li>
    <li><span class="box"></span>Sat</li>
  </ul>
  <div class="slot">
    <span style="left:0;top:0">Date</span>
    <span class="slot-line" style="left:93px;width:288px"></span>
    <span style="left:402px;top:0">AT</span>
    <span class="slot-line" style="left:443px;width:209px"></span>
    <span class="meridiem">am.<br>pm.</span>
  </div>
  <p class="web">KEYSTONEFLOORSOUTLET.COM</p>
</section>

<!-- Outside team: front -->
<section class="card card-front" style="top:1211px">
  <p class="company-name">Keystone<br>Carpet + Flooring</p>
  <p class="motto">craft first</p>
  <div class="person"><span class="person-name">Owen Brandt</span><span class="person-role">Project Manager + Lead Estimator</span></div>
  <div class="rule"></div>
  <ul class="contact">
    <li><span class="icon"><svg width="10" height="16" viewBox="0 0 10 16"><rect x="1" y="1" width="8" height="14" rx="1.5" fill="none" stroke="#fff" stroke-width="1.4"/><rect x="3" y="3" width="4" height="7" fill="#fff"/></svg></span>941 555 0187</li>
    <li><span class="icon"><svg width="16" height="12" viewBox="0 0 16 12"><rect x="1" y="1" width="14" height="10" fill="none" stroke="#fff" stroke-width="1.4"/><path d="M1 1l7 6 7-6" fill="none" stroke="#fff" stroke-width="1.4"/></svg></span>owen@keystonefloorsoutlet.com</li>
  </ul>
  <address class="address">1470 Harbor Mill Rd.<br>Venice, FL 34285</address>
  <svg class="stripe" viewBox="0 0 836 40"><path d="M0 18H470L464 40H0Z" fill="#8f8681"/><path d="M484 0H836V40H476Z" fill="#e08b26"/></svg>
</section>

<!-- Outside team: slogan back -->
<section class="card card-back" style="top:1722px">
  <p class="headline" style="top:162px"><span class="headline-lead">Keystone</span> flooring at<span class="headline-line2">an affordable price</span></p>
  <p class="web">KEYSTONEFLOORSOUTLET.COM</p>
</section>

</body>
</html>
```